Health Coaching Flyer for New Clients

I need a two-sided flyer (3.5" x 8.5" preferred or 5" x 7") to distribute to potential coaching clients. My business name is Talvora Health & Wellness Coaching. My business is focused on helping people with habit changes that contribute to their overall well-being. I would like the design colors to be gender neutral. I would like a small photo of myself near the "my name is Jen" statement. Please feel free to change the logo color to match the design.

Target Market(s)

Adults of all ages.

Font styles to use
Serif

Requirements
Must have
• Emphasize my opening question (found in health coaching brochure - attached).
• Small picture of myself near "my name is Jen" statement.
Should not have
• No light of pastel colors.

```html
<!DOCTYPE html>
<html lang="en">
<head>
<meta charset="utf-8">
<title>Talvora Health &amp; Wellness Coaching – Flyer</title>
<link href="https://fonts.googleapis.com/css2?family=Oswald:wght@300;400&family=Tinos:wght@400;700&family=Playball&display=swap" rel="stylesheet">
<style>
  :root{
    --navy:#0d1b2c;
    --teal:#0a8c7b;
    --teal-deep:#06705f;
    --white:#ffffff;
    --page:#e8e8e8;
    --ink:#0d1b2c;
  }
  *{box-sizing:border-box;margin:0;padding:0}
  html,body{width:1029px;height:1200px;overflow:hidden;background:var(--page)}
  .canvas{position:relative;width:1029px;height:1200px}
  .flyer{position:absolute;top:36px;width:464px;height:1128px;overflow:hidden;box-shadow:6px 8px 14px rgba(0,0,0,.35)}
  .flyer--front{left:29px}
  .flyer--back{left:536px}
  .flyer__art{position:absolute;inset:0;width:100%;height:100%}
  .serif{font-family:"Tinos","Times New Roman",serif;font-weight:700;color:var(--white);white-space:nowrap}

  /* front */
  .brand{position:absolute;top:26px;left:0;width:100%;text-align:center;color:var(--white);font-family:"Tinos","Times New Roman",serif;font-weight:700}
  .brand__name{display:block;font-size:50px;letter-spacing:7px;line-height:52px}
  .brand__tag{display:block;font-size:12px;letter-spacing:.8px;margin-top:2px}
  .headline{position:absolute;top:138px;left:54px;padding-left:13px;border-left:12px solid var(--white);
    font-family:"Oswald",Arial,sans-serif;font-weight:300;color:var(--white);font-size:35px;line-height:46.5px;text-transform:uppercase;letter-spacing:-.2px;white-space:nowrap}
  .intro{position:absolute;top:346px;left:50px;font-family:"Playball",cursive;color:var(--white);font-size:42px;line-height:51px}
  .portrait{position:absolute;top:316px;left:261px;width:161px;height:161px;background:var(--white);padding:14px;box-shadow:3px 4px 10px rgba(0,0,0,.3)}
  .portrait__fill{width:100%;height:100%;background:linear-gradient(160deg,#6b3d2a 0%,#c9927a 50%,#4a2a1e 100%)}
  .story{position:absolute;top:514px;left:48px;font-size:22px;line-height:31.5px;letter-spacing:.5px}
  .story p{margin-bottom:31px}

  /* back */
  .back-title{position:absolute;top:26px;left:35px;padding-left:12px;border-left:12px solid var(--white);
    font-family:"Oswald",Arial,sans-serif;font-weight:300;color:var(--white);font-size:35px;line-height:46px;text-transform:uppercase;white-space:nowrap}
  .benefits{position:absolute;top:124px;left:34px;list-style:none;font-size:19.5px;line-height:25.5px;letter-spacing:.6px}
  .benefits li{margin-bottom:20px}
  .benefits li::before{content:"• "}
  .invite{position:absolute;top:601px;left:34px;font-size:20px;line-height:25.5px;letter-spacing:.5px}
  .invite p{margin-bottom:25.5px}
  .contact{position:absolute;top:913px;left:0;width:100%;text-align:center;color:var(--ink);font-family:"Tinos","Times New Roman",serif;font-weight:700;white-space:nowrap}
  .contact__call{font-size:19.5px;line-height:25.5px;letter-spacing:.5px}
  .contact__name{margin-top:19px;font-size:25px;line-height:30px;letter-spacing:.5px}
  .contact__phone{margin-top:3px;font-size:46px;line-height:52px;letter-spacing:.5px}
  .contact__email{font-size:25px;line-height:28px;letter-spacing:.5px}
</style>
</head>
<body>
<main class="canvas">

  <section class="flyer flyer--front">
    <svg class="flyer__art" viewBox="0 0 619 1504" preserveAspectRatio="none" aria-hidden="true">
      <rect width="619" height="1504" fill="var(--navy)"/>
      <polygon points="0,10 619,830 619,1504 0,1504" fill="var(--teal)"/>
      <polygon points="619,422 619,822 562,642" fill="var(--white)"/>
      <polygon points="0,1000 590,1080 0,1440" fill="var(--teal-deep)" opacity=".45"/>
      <polygon points="392,1372 619,1262 619,1504 575,1504" fill="var(--white)"/>
      <polygon points="0,1442 392,1372 575,1504 0,1504" fill="var(--navy)"/>
    </svg>

    <header class="brand">
      <span class="brand__name">TALVORA</span>
      <span class="brand__tag">HEALTH &amp; WELLNESS COACHING</span>
    </header>

    <h1 class="headline">Need support in making<br>real, lasting lifestyle<br>and behavior changes?</h1>

    <p class="intro">My Name<br>is Jen.</p>
    <figure class="portrait"><div class="portrait__fill" role="img" aria-label="Portrait photo of Jen, the coach"></div></figure>

    <div class="story serif">
      <p>I am studying to become an<br>THRIVE-Certified Functional<br>Health Coach.</p>
      <p>My training involves many<br>science-based practices that<br>improve both our health and<br>how we grow and change as<br>humans.</p>
      <p>I now have the opportunity to<br>turn that knowledge into<br>practice by coaching actual<br>clients interested in improving<br>their own health and<br>well-being.</p>
    </div>
  </section>

  <section class="flyer flyer--back">
    <svg class="flyer__art" viewBox="0 0 619 1504" preserveAspectRatio="none" aria-hidden="true">
      <rect width="619" height="1504" fill="var(--white)"/>
      <polygon points="0,720 619,700 619,1162 0,1202" fill="var(--navy)"/>
      <polygon points="0,0 619,0 619,714 14,762" fill="var(--teal)"/>
    </svg>

    <h2 class="back-title">Functional Health<br>Coaches…</h2>

    <ul class="benefits serif">
      <li>Leverage your strengths rather than<br>focus on your weaknesses</li>
      <li>Support you in finding your own<br>strategies and motivation for change</li>
      <li>Provide a judgment-free zone and<br>support your autonomy</li>
      <li>Use an experimental mindset to find<br>and develop sustainable habits</li>
      <li>Act as your accountability partner as<br>you reach your unique health goals;<br>whether they be improving sleep, diet,<br>fitness, social connection, or reducing<br>stress.</li>
    </ul>

    <div class="invite serif">
      <p>I would like to invite you to<br>participate with me as a client as I<br>continue to hone my coaching skills.<br>We can develop a plan and schedule<br>that aligns with your goals.</p>
      <p>As a way to give back to my<br>community, I am offering new clients<br>six free coaching sessions.&nbsp; This is a<br>limited time offer.</p>
    </div>

    <footer class="contact">
      <p class="contact__call">Please contact me.&nbsp; I’m ready to support<br>you as you work to improve your health.</p>
      <p class="contact__name">Jen Talvora</p>
      <p class="contact__phone">520-555-0193</p>
      <p class="contact__email">talvorahwc@mail.com</p>
    </footer>
  </section>

</main>
</body>
</html>
```